RTV Electrical – Fridge Magnet & Letterbox Leaflet

Overview
We are a local electrical contractor based in Gooseberry Hill in the Perth Hills (Western Australia).
We are looking for a designer to create:
1️⃣ A fridge magnet design
2️⃣ A matching letterbox leaflet (A6 or DL)
The goal is to create clean, professional marketing that feels local and trustworthy, not flashy advertising.
The designs must feel like a high-quality local trades business, appealing to homeowners in suburbs such as:
Kalamunda
Gooseberry Hill
Lesmurdie
Walliston
Pickering Brook
Design Style
The design should feel:
✔ Local
✔ Authentic
✔ Professional
✔ Trustworthy
✔ Clean and simple
NOT:
✖ Cheap advertising
✖ Overly flashy
✖ Busy or cluttered
Think premium local tradesman, not mass marketing.
Branding
Use our brand colours inspired by our van:
Primary colours
Navy Blue
White
Accent colour
Yellow / gold highlight
Design should match the look of our work van branding.
Images Provided
We will provide:
✔ Company logo
✔ Photo of our branded van in the Perth Hills
The van photo should be used in the leaflet design to reinforce our local presence.
Fridge Magnet Design
Size suggestion:
90mm x 55mm
Purpose:
Homeowners keep this magnet so they can easily call a trusted electrician.
Must include:
RTV Electrical Contracting
Local Perth Hills Electrician
Based in Gooseberry Hill
Phone number (large and clear)
📞 0491 726 054
Services:
• Fault finding
• Switchboard upgrades
• Lighting & power
• Ceiling fans
• Smoke alarm compliance
Also include:
⭐ 110+ Starfold Reviews
Website:
www.rtvelectrical.com.au
Design should be very simple and easy to read from across a kitchen.
Leaflet Design
Size options:
A6 or DL
Purpose:
Letterbox drop marketing in Perth Hills suburbs.
Front Side
Headline:
WE'RE WORKING IN YOUR AREA
Subtext:
Local electrician based in Gooseberry Hill
Include:
✔ Photo of our van
✔ RTV logo
✔ Key services
Services:
• Fault finding
• Switchboard upgrades
• Lighting & power
• Ceiling fans
• Smoke alarm compliance
Call to action:
📞 Call Marcus – 0491 726 054
⭐ 110+ Five-Star Starfold Reviews
Back Side
Headline:
Your Local Perth Hills Electrician
Servicing:
Kalamunda
Gooseberry Hill
Lesmurdie
Walliston
Pickering Brook
Short message:
Reliable electrical work across the Perth Hills.
Call Marcus
📞 0491 726 054
Website:
www.rtvelectrical.com.au
EC47286
Target Audience
Homeowners in the Perth Hills aged 35–70.
Many homes are older properties and often need electrical upgrades, repairs and safety work.
Design should appeal to homeowners who value reliability and local service.
Deliverables
Designers must provide:
✔ Print-ready files
✔ Editable source files
✔ High resolution files
For:
Fridge magnet
Leaflet front and back
Final Notes
This design should communicate:
✔ Trusted local electrician
✔ Established business
✔ Professional service
✔ Easy to contact
The goal is to create marketing people will keep, not throw away.

```html
<!DOCTYPE html>
<html lang="en">
<head>
<meta charset="utf-8">
<title>RTV Electrical – Leaflets &amp; Fridge Magnet</title>
<link rel="stylesheet" href="https://fonts.googleapis.com/css2?family=Montserrat:ital,wght@0,500;0,600;0,700;0,800;1,600;1,800&family=Oswald:wght@600;700&display=swap">
<style>
:root{
  --navy:#0f2a63;
  --navy-deep:#0a1f4d;
  --blue:#1f4fb3;
  --blue-bright:#2a62d0;
  --headline:#183d8f;
  --gold:#f7b928;
  --white:#ffffff;
  --stage:#e4e4e4;
}
*{box-sizing:border-box;margin:0;padding:0}
html,body{width:1200px;height:1137px;overflow:hidden}
body{background:var(--stage);font-family:"Montserrat",Arial,sans-serif;color:var(--navy);position:relative}

.leaflet,.magnet{position:absolute;background:var(--white);overflow:hidden;box-shadow:0 1px 4px rgba(0,0,0,.18)}
.leaflet{top:171px;width:398px;height:796px}
.leaflet--front{left:30px}
.leaflet--back{left:452px;width:396px}

/* header */
.brand-band{position:absolute;left:0;top:0;width:100%;height:153px;background:linear-gradient(180deg,var(--blue-bright),var(--blue) 60%,#1a43a0)}
.brand-mark{position:absolute;left:16px;top:18px;width:118px;height:118px;background:var(--navy-deep);border-radius:10px}
.brand-name{position:absolute;left:150px;top:20px;color:var(--white);font-weight:700;line-height:1;text-transform:uppercase;white-space:nowrap}
.brand-name .big{display:block;font-size:58px;letter-spacing:1px}
.brand-name .small{display:block;font-size:21px;line-height:1.1;margin-top:6px}
.license{position:absolute;top:160px;left:208px;font-size:13px;font-weight:600;color:var(--navy)}

/* front */
.area-intro{position:absolute;top:192px;width:100%;text-align:center;font-size:21px;font-weight:800;color:var(--navy)}
.van-photo{position:absolute;left:0;top:250px;width:100%;height:270px;background:linear-gradient(180deg,#eaf2fb 0%,#c9dcef 40%,#8fa57c 66%,#2450ae 72%,#1b3f93 88%,#ffffff 100%)}
.headline{position:absolute;font-family:"Oswald",Impact,sans-serif;font-weight:700;color:var(--headline);line-height:1;text-transform:uppercase;white-space:nowrap;transform-origin:left top}
.headline--suburb{left:40px;top:224px;font-size:64px;transform:scaleX(.88)}
.headline--hill{left:40px;top:290px;font-size:64px;transform:scaleX(.88)}
.sub-local{position:absolute;left:180px;top:296px;font-size:27px;font-weight:600;line-height:1.05;color:var(--navy);text-transform:uppercase;white-space:nowrap}
.bolt-small{position:absolute;left:150px;top:296px;width:24px;height:56px}
.review-badge{position:absolute;left:274px;top:482px;width:104px;height:104px}
.review-badge text{font-family:"Montserrat",Arial,sans-serif;fill:var(--navy);text-anchor:middle}

.services{position:absolute;list-style:none;white-space:nowrap}
.services--front{left:36px;top:553px;font-size:17px;font-weight:600;line-height:21.6px;color:var(--navy)}
.services--front li{display:flex;align-items:center;gap:8px}
.tick{width:12px;height:14px;flex:none}

/* back */
.bolt-head{position:absolute;left:48px;top:210px;width:30px;height:92px}
.headline--area{left:88px;top:214px;font-size:64px;transform:scaleX(.94)}
.sub-area{position:absolute;left:90px;top:282px;font-size:26px;font-weight:600;color:var(--navy);text-transform:uppercase;white-space:nowrap}
.rule{position:absolute;left:40px;width:322px;height:2px;background:var(--gold)}
.rule--top{top:322px}
.rule--bottom{top:401px}
.tagline{position:absolute;top:336px;width:100%;text-align:center;font-size:20px;font-weight:800;font-style:italic;line-height:1.25;color:var(--navy)}
.tag-service{position:absolute;left:40px;top:408px;width:170px;height:23px;background:var(--gold);clip-path:polygon(0 0,100% 0,92% 100%,0 100%);font-size:13px;font-weight:800;color:var(--navy);padding:4px 0 0 22px}
.services--area{left:34px;top:450px;font-size:17px;font-weight:600;line-height:30.7px;color:var(--navy)}
.services--area li::before{content:"•";margin-right:8px}
.worker-photo{position:absolute;left:213px;top:431px;width:183px;height:246px;background:linear-gradient(160deg,#f2f4f7,#d9dde3 45%,#7e8694 80%,#f5f5f5)}

/* contact foot */
.contact{position:absolute;left:112px;bottom:0;width:calc(100% - 112px);height:119px;background:var(--navy);clip-path:polygon(8% 0,100% 0,100% 100%,0 100%)}
.contact .call{position:absolute;right:22px;top:12px;font-size:21px;font-weight:500;color:var(--white)}
.contact .phone{position:absolute;right:22px;top:36px;font-size:32px;font-weight:700;color:var(--white);letter-spacing:.5px;white-space:nowrap}
.web-bar{position:absolute;left:9px;bottom:0;width:304px;height:36px;background:var(--blue);clip-path:polygon(0 0,100% 0,93% 100%,0 100%);color:var(--white);font-size:15px;font-weight:700;padding:10px 0 0 32px;white-space:nowrap}

/* magnet */
.magnet{left:876px;top:487px;width:293px;height:478px;border-radius:22px}
.magnet .brand-mark{left:26px;top:20px;width:104px;height:104px}
.magnet .brand-name{left:146px;top:22px;color:var(--navy)}
.magnet .brand-name .big{font-size:56px;letter-spacing:0}
.magnet .brand-name .small{font-size:17px;margin-top:8px;line-height:1.15}
.magnet-panel{position:absolute;left:0;top:178px;width:100%;height:232px;background:var(--navy)}
.magnet-tag{position:absolute;left:26px;top:192px;font-size:16px;font-weight:600;font-style:italic;color:var(--white)}
.services--magnet{left:26px;top:230px;font-size:15px;font-weight:700;line-height:19.3px;color:var(--white)}
.services--magnet li::before{content:"•";color:var(--gold);margin-right:6px}
.bolt-magnet{position:absolute;left:232px;top:172px;width:60px;height:184px}
.phone-box{position:absolute;left:28px;top:357px;width:239px;height:45px;background:var(--gold);border-radius:6px;border:2px solid #ffd865;display:flex;align-items:center;justify-content:center;gap:10px;font-family:"Oswald",Impact,sans-serif;font-weight:600;font-size:31px;color:var(--navy);white-space:nowrap}
.phone-icon{width:24px;height:24px}
.magnet-reviews{position:absolute;top:412px;width:100%;text-align:center;font-size:20px;font-weight:500;color:var(--navy)}
.magnet-reviews b{font-weight:800}
.magnet-rule{position:absolute;left:28px;top:440px;width:237px;height:2px;background:var(--gold)}
.magnet-web{position:absolute;top:447px;width:100%;text-align:center;font-size:17px;font-weight:800;color:var(--navy)}
</style>
</head>
<body>

<section class="leaflet leaflet--front">
  <header class="brand-band">
    <span class="brand-mark"></span>
    <p class="brand-name"><span class="big">RTV</span><span class="small">Electrical<br>Contracting</span></p>
  </header>
  <div class="van-photo" role="img" aria-label="Photo of the RTV Electrical branded work van parked in the Perth Hills bush"></div>
  <p class="area-intro">We are working in your area!</p>
  <h1 class="headline headline--suburb">Gooseberry</h1>
  <p class="headline headline--hill">Hill</p>
  <svg class="bolt-small" viewBox="0 0 24 56"><polygon points="14,0 2,30 11,30 6,56 22,22 13,22 20,0" fill="#f7b928"/></svg>
  <p class="sub-local">Local<br>Electrician</p>
  <svg class="review-badge" viewBox="0 0 104 104" role="img" aria-label="110 plus five-star Starfold Reviews">
    <polygon fill="#f7b928" points="52,2 60,10 71,6 75,17 86,18 85,29 95,35 89,44 95,52 89,60 95,69 85,75 86,86 75,87 71,98 60,94 52,102 44,94 33,98 29,87 18,86 19,75 9,69 15,60 9,52 15,44 9,35 19,29 18,18 29,17 33,6 44,10"/>
    <text x="52" y="38" font-size="17" font-weight="800">110+</text>
    <text x="52" y="56" font-size="13">★★★★★</text>
    <text x="52" y="71" font-size="12" font-weight="600">Starfold</text>
    <text x="52" y="85" font-size="12" font-weight="600">Reviews</text>
  </svg>
  <ul class="services services--front">
    <li><svg class="tick" viewBox="0 0 12 14"><path d="M1 8 L4 12 L11 1" stroke="#0f2a63" stroke-width="1.8" fill="none"/></svg>Fault finding</li>
    <li><svg class="tick" viewBox="0 0 12 14"><path d="M1 8 L4 12 L11 1" stroke="#0f2a63" stroke-width="1.8" fill="none"/></svg>Switchboard upgrades</li>
    <li><svg class="tick" viewBox="0 0 12 14"><path d="M1 8 L4 12 L11 1" stroke="#0f2a63" stroke-width="1.8" fill="none"/></svg>Lighting &amp; power</li>
    <li><svg class="tick" viewBox="0 0 12 14"><path d="M1 8 L4 12 L11 1" stroke="#0f2a63" stroke-width="1.8" fill="none"/></svg>Ceiling fans</li>
    <li><svg class="tick" viewBox="0 0 12 14"><path d="M1 8 L4 12 L11 1" stroke="#0f2a63" stroke-width="1.8" fill="none"/></svg>Smoke alarm compliance</li>
  </ul>
  <footer class="contact">
    <p class="call">Call Marcus</p>
    <p class="phone">0491 726 054</p>
  </footer>
  <p class="web-bar">WWW.RTVELECTRICAL.COM.AU</p>
</section>

<section class="leaflet leaflet--back">
  <header class="brand-band">
    <span class="brand-mark"></span>
    <p class="brand-name"><span class="big">RTV</span><span class="small">Electrical<br>Contracting</span></p>
  </header>
  <p class="license">License: EC47286</p>
  <svg class="bolt-head" viewBox="0 0 30 92"><polygon points="18,0 2,50 13,50 6,92 28,36 17,36 26,0" fill="#f7b928"/></svg>
  <h1 class="headline headline--area">Perth Hill</h1>
  <p class="sub-area">Local Electrician</p>
  <span class="rule rule--top"></span>
  <p class="tagline">Professional service from<br>a trusted local electrician.</p>
  <span class="rule rule--bottom"></span>
  <p class="tag-service">SERVICE AREA</p>
  <ul class="services services--area">
    <li>Kalamunda</li>
    <li>Gooseberry Hill</li>
    <li>Lesmurdie</li>
    <li>Walliston</li>
    <li>Pickering Brook</li>
  </ul>
  <div class="worker-photo" role="img" aria-label="Photo of a smiling electrician in a hard hat carrying coiled cables, giving a thumbs up"></div>
  <footer class="contact">
    <p class="call">Call Marcus</p>
    <p class="phone">0491 726 054</p>
  </footer>
  <p class="web-bar">WWW.RTVELECTRICAL.COM.AU</p>
</section>

<section class="magnet">
  <span class="brand-mark"></span>
  <p class="brand-name"><span class="big">RTV</span><span class="small">Electrical<br>Contracting</span></p>
  <div class="magnet-panel"></div>
  <p class="magnet-tag">Local Perth Hills Electrician</p>
  <ul class="services services--magnet">
    <li>Fault finding</li>
    <li>Switchboard upgrades</li>
    <li>Lighting &amp; power</li>
    <li>Ceiling fans</li>
    <li>Smoke alarm compliance</li>
  </ul>
  <svg class="bolt-magnet" viewBox="0 0 60 184"><polygon points="40,0 4,100 28,100 14,184 58,70 34,70 54,0" fill="#f7b928"/></svg>
  <p class="phone-box">
    <svg class="phone-icon" viewBox="0 0 24 24"><path fill="#0f2a63" d="M6.6 10.8a15.1 15.1 0 0 0 6.6 6.6l2.2-2.2a1 1 0 0 1 1-.25 11.4 11.4 0 0 0 3.6.57 1 1 0 0 1 1 1V20a1 1 0 0 1-1 1A17 17 0 0 1 3 4a1 1 0 0 1 1-1h3.5a1 1 0 0 1 1 1c0 1.25.2 2.45.57 3.57a1 1 0 0 1-.25 1z"/></svg>
    0491 726 054
  </p>
  <p class="magnet-reviews"><b>110+</b> Starfold Reviews</p>
  <span class="magnet-rule"></span>
  <p class="magnet-web">www.rtvelectrical.com.au</p>
</section>

</body>
</html>
```